WordPress Site Clean up

We are a small wireless networking company in Norther Colorado. We have a basic layout to our new website, and require a person or persons who can clean the new site up so we can go live with it in the coming weeks. Our company has the logo and content, we just need to clean the formatting up, improve the colors/graphics. It is currently a ZUNPLIKE. We also need help making our project pictures look better on the website, and clean up the images all around.

The website can be found at: www.4qvtelmora.com/newsite

We can provide you with photos and more content, but we have gone as far as we can with "building" the wordpress site.

It Company

```html
<!DOCTYPE html>
<html lang="en">
<head>
<meta charset="utf-8">
<title>Qvtel Networks</title>
<link href="https://fonts.googleapis.com/css2?family=Lato:ital,wght@0,400;0,700;1,400&family=Roboto+Condensed:wght@400;700&display=swap" rel="stylesheet">
<style>
:root{
  --green:#8cc63f;
  --green-dark:#6fa52c;
  --ink:#333;
  --muted:#666;
  --light:#f3f3f3;
  --footer:#3b3b3b;
  --white:#fff;
  --sky-top:#9fb8cf;
  --sky-low:#dfe6ec;
  --roof:#a0785a;
  --steel:#8e979f;
}
*{box-sizing:border-box;margin:0;padding:0}
html,body{width:1200px;height:3799px;overflow:hidden}
body{font-family:"Lato",sans-serif;color:var(--ink);background:var(--white);font-size:14px}
.heading{font-family:"Roboto Condensed",sans-serif;font-weight:400;text-align:center;font-size:38px;letter-spacing:.5px}
.wave{display:block;margin:6px auto 0}

/* header */
.site-header{height:133px;background:var(--green);color:var(--white);position:relative}
.topbar{height:38px;display:flex;justify-content:space-between;align-items:center;padding:0 70px;font-size:12px;border-bottom:1px solid rgba(255,255,255,.25)}
.topbar .follow{display:flex;align-items:center;gap:6px}
.topbar .dot{width:12px;height:12px;border-radius:50%;background:var(--white)}
.brand{position:absolute;left:70px;top:52px;font-size:34px;font-weight:400;display:flex;align-items:center;gap:10px}
.brand .sq{width:14px;height:14px;background:var(--white)}
.nav{position:absolute;right:40px;top:38px;display:flex;height:89px}
.nav a{color:var(--white);text-decoration:none;font-size:15px;padding:0 18px;display:flex;align-items:center}
.nav a.active{background:var(--green-dark)}

/* hero */
.hero{height:491px;position:relative;background:
  linear-gradient(90deg,rgba(0,0,0,0) 40%,rgba(0,0,0,.35) 100%),
  linear-gradient(180deg,#eef0f2 0%,#c9ced3 38%,#8d949a 62%,#6b7278 100%)}
.hero-copy{position:absolute;left:615px;top:75px;width:480px;color:var(--white)}
.hero-copy h1{font-family:"Lato",sans-serif;font-weight:400;font-size:38px;line-height:1.25}
.hero-copy p{font-size:13px;line-height:1.5;margin-top:14px}
.btn{display:inline-flex;align-items:center;gap:10px;background:var(--green);color:var(--white);font-size:14px;font-weight:700;padding:0 22px;height:42px;text-transform:uppercase;white-space:nowrap}
.hero-copy .btn{margin-top:58px}
.dots{position:absolute;left:0;right:0;bottom:22px;display:flex;justify-content:center;gap:8px}
.dots span{width:11px;height:11px;border-radius:50%;background:rgba(255,255,255,.6)}
.dots span.on{background:var(--green)}

/* about */
.about{height:468px;padding-top:68px}
.about .intro{font-style:italic;text-align:center;width:1090px;margin:24px auto 0;font-size:14px;line-height:1.6}
.services{display:flex;justify-content:space-between;padding:0 70px;margin-top:48px}
.service{width:330px}
.service h3{display:flex;align-items:center;gap:12px;font-size:24px;font-weight:400}
.service p{font-size:13px;line-height:1.6;color:var(--muted);margin-top:16px}
.more{color:var(--green);font-size:13px;margin-top:26px;display:block}

/* what we do */
.whatwedo{height:611px;background:linear-gradient(180deg,#1f2830,#36424d 60%,#2a333c);color:var(--white);position:relative;padding-top:58px}
.whatwedo .lead{font-style:italic;text-align:center;width:1050px;margin:28px auto 0;line-height:1.6}
.tooltip{position:absolute;left:528px;top:196px;width:228px;background:var(--white);color:var(--ink);font-size:12px;line-height:1.5;text-align:center;padding:10px 14px}
.tooltip::after{content:"";position:absolute;left:104px;bottom:-10px;border:10px solid transparent;border-bottom:0;border-top-color:var(--white)}
.values{position:absolute;left:60px;right:60px;top:338px;display:flex;justify-content:space-between}
.value{width:180px;text-align:center}
.value .label{font-size:17px;height:40px}
.value.active .label{color:var(--green)}
.value .ring{width:172px;height:172px;margin:0 auto;border-radius:50%;border:8px solid var(--white);background:linear-gradient(180deg,var(--sky-low) 0%,#b9c0c6 45%,#6d7379 100%)}
.value.active .ring{border-color:var(--green);background:var(--green)}
.connector{position:absolute;left:150px;right:150px;top:462px;height:3px;background:var(--white)}

/* projects */
.projects{height:773px;padding-top:50px}
.projects .sub{font-style:italic;text-align:center;margin-top:22px}
.grid{display:grid;grid-template-columns:repeat(4,248px);gap:23px 22px;padding:0 70px;margin-top:40px}
.tile{height:250px}
.tile.sky{background:linear-gradient(180deg,var(--sky-top) 0%,var(--sky-low) 70%,#c8ccd0 100%)}
.tile.roof{background:linear-gradient(180deg,var(--sky-top) 0%,var(--sky-low) 45%,var(--roof) 60%,#7b5a44 100%)}
.tile.steel{background:linear-gradient(160deg,#b5bcc2,#5f676e)}
.tile.town{background:linear-gradient(180deg,#7fa4c8 0%,#c6d5e2 50%,#a59a8a 70%,#8a7f70 100%)}
.tile.dish{background:linear-gradient(180deg,#cfd3d6 0%,var(--steel) 100%)}
.tile.feature{background:var(--green);color:var(--white);display:flex;flex-direction:column;align-items:center;justify-content:center;gap:22px;font-size:15px;text-align:center}
.tile.feature .icons{display:flex;gap:14px}

/* team */
.team{height:658px;background:var(--green);color:var(--white);padding-top:48px}
.team .lead{font-style:italic;text-align:center;width:900px;margin:28px auto 0;line-height:1.6}
.cards{display:flex;justify-content:space-between;padding:0 73px;margin-top:38px}
.card{width:238px}
.card .photo{height:241px;position:relative;background:linear-gradient(180deg,#b7b9ae 0%,#9a9c8f 45%,#c9a48a 46%,#b78d72 75%,#56688a 76%,#45556f 100%)}
.card:nth-child(2) .photo{background:linear-gradient(180deg,#c2c5c8 0%,#a9adb1 45%,#d0a98e 46%,#bb9277 75%,#6f8fc0 76%,#5a79a8 100%)}
.card:nth-child(4) .photo{background:linear-gradient(180deg,#a9a39a 0%,#8f897f 45%,#d6ab8e 46%,#c29274 75%,#3a3a3a 76%,#262626 100%)}
.card .info{height:190px;background:var(--white);color:var(--ink);text-align:center;padding:20px 18px}
.card .info h4{font-size:17px}
.card .info .role{font-size:13px;color:var(--muted);margin-top:2px}
.card .info p{font-size:12px;line-height:1.5;color:var(--muted);margin-top:12px}
.card.active .photo{background:linear-gradient(180deg,#4a4a4a,#262626)}
.card.active .info{background:#2e2e2e;color:var(--white)}
.card.active .info h4{color:var(--white)}
.card.active .info .role,.card.active .info p{color:#ddd}
.socials{position:absolute;left:0;right:0;bottom:16px;display:flex;justify-content:center;gap:8px}
.socials span{width:26px;height:26px;background:var(--green)}

/* partners */
.partners{height:396px;padding-top:50px}
.partners .sub{font-style:italic;text-align:center;width:900px;margin:24px auto 0;line-height:1.6}
.badges{display:flex;justify-content:space-between;padding:0 73px;margin-top:44px}
.badge{width:238px;height:105px;border:1px solid #ddd;display:flex;align-items:center;justify-content:center}
.badge span{width:120px;height:36px;background:#d5d5d5;border-radius:4px}

/* newsletter */
.newsletter{height:206px;background:var(--light);display:flex;align-items:center;padding:0 70px;gap:30px}
.newsletter h2{font-family:"Lato",sans-serif;font-weight:400;font-size:26px;line-height:1.25;width:200px;flex:none}
.field{width:310px;height:46px;background:var(--white);border:1px solid #ddd;color:#999;font-size:13px;display:flex;align-items:center;padding:0 14px;flex:none}
.newsletter .btn{margin-left:auto;flex:none}

/* footer */
.site-footer{height:63px;background:var(--footer);color:#ccc;display:flex;align-items:center;justify-content:space-between;padding:0 70px;font-size:12px}
.site-footer .follow{display:flex;gap:8px}
.site-footer .follow span{width:26px;height:26px;border-radius:50%;background:#777}
</style>
</head>
<body>

<header class="site-header">
  <div class="topbar">
    <span>&#9742; Call Us: 1-800-555-0142</span>
    <span class="follow">Follow us <i class="dot"></i><i class="dot"></i><i class="dot"></i><i class="dot"></i></span>
  </div>
  <div class="brand"><span class="sq"></span>Qvtel Networks</div>
  <nav class="nav">
    <a class="active">Home</a><a>About Us</a><a>Services</a><a>Technology</a><a>Partner</a><a>Blog</a><a>Contact Us</a>
  </nav>
</header>

<section class="hero" role="img" aria-label="Wireless antennas mounted on a rooftop mast above a city">
  <div class="hero-copy">
    <h1>All your wireless needs a professional solution</h1>
    <p>Lorem ipsum dolor sit amet, consectetur adipiscing elit, sed do eiusmod tempor incididunt ut labore et dolore magna aliqua. Ut enim ad minim veniam, quis nostrud exercitation ullamco laboris nisi ut aliquip ex ea commodo consequat.</p>
    <span class="btn">Learn More <svg width="14" height="14" viewBox="0 0 14 14"><circle cx="7" cy="7" r="7" fill="#fff"/><path d="M5 4l3 3-3 3" stroke="#8cc63f" stroke-width="2" fill="none"/></svg></span>
  </div>
  <div class="dots"><span class="on"></span><span></span><span></span></div>
</section>

<section class="about">
  <h2 class="heading">About Us</h2>
  <svg class="wave" width="90" height="8" viewBox="0 0 90 8"><path d="M0 4 Q7.5 0 15 4 T30 4 T45 4 T60 4 T75 4 T90 4" stroke="#8cc63f" stroke-width="2" fill="none"/></svg>
  <p class="intro">Lorem Ipsum is simply dummy text of the printing and typesetting industry. Lorem Ipsum has been the industry's standard dummy text ever since the 1500s, when an unknown printer took a galley of type and scrambled it to make a type specimen book. It has survived not only five centuries, but also the leap into electronic typesetting, remaining essentially unchanged.</p>
  <div class="services">
    <div class="service">
      <h3><svg width="30" height="30" viewBox="0 0 30 30"><rect x="7" y="7" width="16" height="16" fill="none" stroke="#8cc63f" stroke-width="3"/><path d="M11 2v5M19 2v5M11 23v5M19 23v5M2 11h5M2 19h5M23 11h5M23 19h5" stroke="#8cc63f" stroke-width="2"/></svg>Technology</h3>
      <p>Providing world class services is Qvtel Network's commitment. We provide a whole host of services from installation to design work.</p>
      <span class="more">Learn More &rarr;</span>
    </div>
    <div class="service">
      <h3><svg width="30" height="30" viewBox="0 0 30 30"><circle cx="15" cy="15" r="13" fill="#8cc63f"/><path d="M8 15l5 5 9-10" stroke="#fff" stroke-width="3" fill="none"/></svg>Solutions</h3>
      <p>We are a vendor neutral solution provider. We carefully learn the needs of our customers and fit them with the right solution.</p>
      <span class="more">Learn More &rarr;</span>
    </div>
    <div class="service">
      <h3><svg width="30" height="30" viewBox="0 0 30 30"><path d="M5 25l3-9 14-14 6 6-14 14z" fill="#8cc63f"/></svg>Design</h3>
      <p>Designing networks is a combination of science, standards and a little bit of art. Many IT companies can sell you the equipment, but not only sell it ...</p>
      <span class="more">Learn More &rarr;</span>
    </div>
  </div>
</section>

<section class="whatwedo">
  <h2 class="heading">WHAT WE DO</h2>
  <p class="lead">We live in a digital world that is connected. We are here to make those connections, and help our customers succeed. Whatever your IT need or goal is, we will strive to meet and exceed your expectations.</p>
  <div class="tooltip">Qvtel Networks makes safety priority one for both the customer and its employees. Qvtel Networks stays current on the latest industry standards and exceeds them in providing services and products.</div>
  <div class="connector"></div>
  <div class="values">
    <div class="value"><div class="label">Our Solutions</div><div class="ring" role="img" aria-label="Antenna equipment photo"></div></div>
    <div class="value"><div class="label">Customer Focus</div><div class="ring" role="img" aria-label="Antenna equipment photo"></div></div>
    <div class="value active"><div class="label">Safety First</div><div class="ring" role="img" aria-label="Safety highlight"></div></div>
    <div class="value"><div class="label">Professionalism</div><div class="ring" role="img" aria-label="Antenna equipment photo"></div></div>
    <div class="value"><div class="label">Quality</div><div class="ring" role="img" aria-label="Antenna equipment photo"></div></div>
  </div>
</section>

<section class="projects">
  <h2 class="heading">OUR LATEST PROJECTS</h2>
  <svg class="wave" width="90" height="8" viewBox="0 0 90 8"><path d="M0 4 Q7.5 0 15 4 T30 4 T45 4 T60 4 T75 4 T90 4" stroke="#8cc63f" stroke-width="2" fill="none"/></svg>
  <p class="sub">Take a look at our latest projects and learn more about what we can do for you and your networking needs.</p>
  <div class="grid">
    <div class="tile dish" role="img" aria-label="Dish antenna on a rooftop"></div>
    <div class="tile roof" role="img" aria-label="Wireless radio mounted on a building roof"></div>
    <div class="tile feature">
      <div class="icons">
        <svg width="40" height="40" viewBox="0 0 40 40"><circle cx="20" cy="20" r="19" fill="none" stroke="#fff" stroke-width="2"/><path d="M15 25l10-10M17 15h8v8" stroke="#fff" stroke-width="2" fill="none"/></svg>
        <svg width="40" height="40" viewBox="0 0 40 40"><circle cx="20" cy="20" r="19" fill="none" stroke="#fff" stroke-width="2"/><circle cx="18" cy="18" r="6" fill="none" stroke="#fff" stroke-width="2"/><path d="M22 22l6 6M15 18h6M18 15v6" stroke="#fff" stroke-width="2"/></svg>
      </div>
      <div>Wireless Solution<br>Lumber Yard</div>
    </div>
    <div class="tile sky" role="img" aria-label="Antenna mast against the sky"></div>
    <div class="tile steel" role="img" aria-label="Network equipment cabinet"></div>
    <div class="tile town" role="img" aria-label="Radio mounted above a town"></div>
    <div class="tile roof" role="img" aria-label="Rooftop radio installation"></div>
    <div class="tile dish" role="img" aria-label="Dish antenna on a pole"></div>
  </div>
</section>

<section class="team">
  <h2 class="heading">MEET OUR AMAZING TEAM</h2>
  <svg class="wave" width="90" height="8" viewBox="0 0 90 8"><path d="M0 4 Q7.5 0 15 4 T30 4 T45 4 T60 4 T75 4 T90 4" stroke="#fff" stroke-width="2" fill="none"/></svg>
  <p class="lead">Experience is what drives our team. With our combination of experience and knowledge, we can solve your problems and provide you with knowledge to help you make decisions.</p>
  <div class="cards">
    <div class="card"><div class="photo" role="img" aria-label="Portrait of the founder"></div><div class="info"><h4>Marten Oakhill</h4><div class="role">CEO, Founder</div><p>Marten Oakhill has 24+ years of experience in the data networking industry.</p></div></div>
    <div class="card"><div class="photo" role="img" aria-label="Portrait of the sales VP"></div><div class="info"><h4>Dale Oakhill</h4><div class="role">VP of Sales and Marketing</div><p>Dale Oakhill has 12+ years experience in sales in wireless networking.</p></div></div>
    <div class="card active"><div class="photo" role="img" aria-label="Portrait of the sales executive"><div class="socials"><span></span><span></span><span></span><span></span></div></div><div class="info"><h4>Rory Fenwick</h4><div class="role">Sales Executive</div><p>Rory Fenwick has 30+ years experience in sales and customer service.</p></div></div>
    <div class="card"><div class="photo" role="img" aria-label="Portrait of the systems engineer"></div><div class="info"><h4>TJ Calloway</h4><div class="role">Systems Engineer</div><p>TJ has 6+ years experience in desktop support and network engineering.</p></div></div>
  </div>
</section>

<section class="partners">
  <h2 class="heading">OUR PARTNERS</h2>
  <svg class="wave" width="90" height="8" viewBox="0 0 90 8"><path d="M0 4 Q7.5 0 15 4 T30 4 T45 4 T60 4 T75 4 T90 4" stroke="#8cc63f" stroke-width="2" fill="none"/></svg>
  <p class="sub">Qvtel Networks partners with the market leaders in networking technologies. We are committed to delivering the right product for your need, everytime.</p>
  <div class="badges">
    <div class="badge"><span></span></div>
    <div class="badge"><span></span></div>
    <div class="badge"><span></span></div>
    <div class="badge"><span></span></div>
  </div>
</section>

<section class="newsletter">
  <h2>Signup to<br>Our Newsletter</h2>
  <div class="field">Enter your name</div>
  <div class="field">Enter your email</div>
  <span class="btn">Learn More <svg width="14" height="14" viewBox="0 0 14 14"><circle cx="7" cy="7" r="7" fill="#fff"/><path d="M5 4l3 3-3 3" stroke="#8cc63f" stroke-width="2" fill="none"/></svg></span>
</section>

<footer class="site-footer">
  <span>&copy; Copyright 2015, qvtelnetworks.com | All Rights Reserved</span>
  <span class="follow"><span></span><span></span><span></span><span></span></span>
</footer>

</body>
</html>
```